Design 2 Print Banners for Conference Booth

We need a tall banner and a table banner rough designed for our Conference Booth. The link shows the current booth and what details for banner dimensions and text
see complete design brief here .. https://files.brindlepaper.net/doc/7QkTzR2mWpXa9LcVn4HsJd8EyBfU3oGtKiN6/view?mode=shared

Target Market(s)

Doctors & Medical Professionals

Industry/Entity Type

Google

Colors
33a6d7
cee9f5
ecf7fb

Requirements
Must have
• match our branding colors - see current booth backdrop and our website quietoaktesting.com

```html
<!DOCTYPE html>
<html lang="en">
<head>
<meta charset="utf-8">
<title>Quiet Oak Testing – Roll-up Banner</title>
<link rel="stylesheet" href="https://fonts.googleapis.com/css2?family=Arimo:wght@400;700&display=swap">
<style>
  :root {
    --stage: #e4e4e4;
    --paper: #ffffff;
    --mist: #dde4ea;
    --sky: #5cbbe3;
    --ocean: #33a6d7;
    --deep-ocean: #2a93c4;
    --gold: #e9b44c;
    --amber: #d49a2e;
    --teal-ink: #1f6a86;
    --brand-ink: #3f8fa6;
    --body-ink: #3a3a3a;
    --muted-ink: #777777;
    --field-green: #6f8a3e;
    --field-dark: #3f5a26;
    --bloom: #e8c02a;
  }
  * { margin: 0; padding: 0; box-sizing: border-box; }
  html, body {
    width: 1200px; height: 900px; overflow: hidden;
    background: var(--stage);
    font-family: 'Arimo', Arial, sans-serif;
  }
  .stage {
    position: relative; width: 1200px; height: 900px;
    display: flex; align-items: center; justify-content: center;
  }
  .banner {
    position: relative; width: 300px; height: 870px; overflow: hidden;
    background: linear-gradient(180deg, var(--paper) 0%, var(--paper) 36%, var(--mist) 62%, var(--mist) 100%);
    box-shadow: 0 2px 10px rgba(0,0,0,0.12);
  }
  .swoosh { position: absolute; left: 0; width: 100%; display: block; }
  .swoosh--top { top: 0; height: 80px; }
  .swoosh--bottom { bottom: 0; height: 110px; z-index: 2; }

  .brand {
    position: absolute; top: 104px; left: 0; width: 100%;
    display: flex; align-items: center; justify-content: center; gap: 10px;
  }
  .brand__mark {
    width: 34px; height: 34px; border-radius: 50%; background: var(--brand-ink);
  }
  .brand__name {
    color: var(--brand-ink); font-weight: 400; text-align: center; line-height: 1;
  }
  .brand__name-main { display: block; font-size: 31px; letter-spacing: -0.5px; }
  .brand__name-sub {
    display: block; font-size: 12px; letter-spacing: 9px; margin-top: 8px;
    padding-top: 6px; border-top: 1px solid var(--brand-ink);
  }

  .testimonial {
    position: absolute; top: 240px; left: 22px; right: 20px;
    color: var(--body-ink);
  }
  .testimonial__quote { font-size: 14px; line-height: 1.3; letter-spacing: -0.2px; }
  .testimonial__cite {
    display: block; text-align: center; font-size: 8px; color: var(--muted-ink);
    margin-top: 6px; font-style: normal;
  }

  .cta { position: absolute; top: 358px; left: 0; width: 100%; text-align: center; }
  .cta__lead { font-size: 21px; color: var(--body-ink); letter-spacing: -0.4px; }
  .cta__action {
    font-size: 31px; font-weight: 700; color: var(--body-ink);
    letter-spacing: -1.2px; margin-top: 4px; line-height: 1.1;
  }
  .cta__number {
    font-size: 46px; font-weight: 700; color: var(--teal-ink);
    letter-spacing: -0.5px; margin-top: 10px; line-height: 1.1;
  }

  .photo {
    position: absolute; left: 0; right: 0; top: 527px; bottom: 0; z-index: 1;
    background:
      radial-gradient(ellipse at 45% 18%, var(--bloom) 0%, rgba(232,192,42,0) 22%),
      linear-gradient(180deg, #c9d2b0 0%, var(--field-green) 30%, var(--field-dark) 75%, #4a6b8a 100%);
  }
</style>
</head>
<body>
<main class="stage">
  <section class="banner" aria-label="Quiet Oak Testing roll-up banner">
    <svg class="swoosh swoosh--top" viewBox="0 0 300 80" preserveAspectRatio="none" aria-hidden="true">
      <path d="M0 0 H150 C100 10 45 18 0 24 Z" fill="var(--gold)"/>
      <path d="M0 24 C70 16 160 6 300 0 V22 C230 62 110 72 0 66 Z" fill="var(--sky)"/>
    </svg>

    <div class="brand">
      <span class="brand__mark" aria-hidden="true"></span>
      <p class="brand__name">
        <span class="brand__name-main">Quiet Oak</span>
        <span class="brand__name-sub">TESTING</span>
      </p>
    </div>

    <blockquote class="testimonial">
      <p class="testimonial__quote">"No single endeavour has had as great a financial impact on our practice as choosing to work with Quiet Oak Testing"</p>
      <cite class="testimonial__cite">- Dana Whitfield, Practice Manager</cite>
    </blockquote>

    <div class="cta">
      <p class="cta__lead">Get the facts instantly</p>
      <p class="cta__action">TEXT ALLERGY TO</p>
      <p class="cta__number">52736</p>
    </div>

    <div class="photo" role="img" aria-label="Photo of a young child smelling a tall sunflower in a sunflower field"></div>

    <svg class="swoosh swoosh--bottom" viewBox="0 0 300 110" preserveAspectRatio="none" aria-hidden="true">
      <path d="M150 40 C210 22 260 14 300 14 V48 C250 46 200 46 150 40 Z" fill="var(--amber)"/>
      <path d="M0 78 C80 30 180 30 300 46 V110 H0 Z" fill="var(--deep-ocean)"/>
    </svg>
  </section>
</main>
</body>
</html>
```